Tito - Idiomas Corvalo

2x Design Concepts for the home page and interior pages based on the attached brief and powerpoint presentation.

Colours: see 2.1 logo and heading for logo colours and website colours

Home Page: (please see attached file)
1)Logo to appear in the top left, heading to include telephone numbers and a best price (credibility stamp) - see 2.1
2)the toolbar is to be centered at the top. Emphasis must be placed on the 5 easy steps to study english in Australia - see 2.2
3) modules. 5x modules required in the home page for: home page image rotator, online quote tool, enquiry form, best deals, quick links (there are 2 examples for the quick links module - open to suggestions) - see 2.3
4) footer. the footer is to include partner logos with hyperlinks to the partner websites. with a copywright section at the base - see 2.4
5) 2.5 is the basic idea - open to design suggestions. The website objective is to submit an online quote or contact Idiomas Corvalo.

Internal Page: - see 3-
open to all suggestion. Require a lot of space for internal custom design concepts (these are taking place inhouse). The interior page must have a side module toolbar to include:
1) a modified online quote tool
2) modified enquiry form
3) modified quick links section

Target Market(s)

target market is young (17-30yrs) Brazilians looking to study English in Australia or continue studying English in Australia that can also acquire visa sponsorship.

The buyer will be the parents of the students. the design must appeal to both markets.

Number of Pages Required

2 pages

Requirements
Must have
• see project overview
2x design concepts for the home page and interior page
professional, clean, simple and easy to navigate

```html
<!DOCTYPE html>
<html lang="pt-BR">
<head>
<meta charset="utf-8">
<title>Idiomas Corvalo</title>
<link href="https://fonts.googleapis.com/css2?family=Questrial&family=PT+Sans:wght@400;700&display=swap" rel="stylesheet">
<style>
:root{
  --blue:#1f5aa6;
  --blue-dark:#1b4787;
  --band:#1d4a8c;
  --green:#0b9b58;
  --green-dark:#078848;
  --link-green:#0a8a50;
  --orange-top:#f7b24a;
  --orange-bot:#e58a12;
  --tab-text:#5b3510;
  --red:#e0261c;
  --text:#555;
  --line:#e3e3e3;
  --gold:#f0c21c;
}
*{box-sizing:border-box;margin:0;padding:0}
html,body{width:1200px;height:2674px;overflow:hidden}
body{font-family:"PT Sans",sans-serif;color:var(--text);background:#fff}
.page{position:relative;width:1200px;overflow:hidden}
.page-home{height:1281px}
.page-inner{height:1393px}
.abs{position:absolute}
.head-bg{left:0;top:0;width:1200px;height:175px;background:repeating-linear-gradient(135deg,#f6f6f6 0 2px,#fbfbfb 2px 4px);border-top:2px solid #cfcfcf}
.band{left:0;top:175px;width:1200px;background:var(--band)}
.brand{left:85px;top:48px;font-family:"Questrial",sans-serif;font-size:30px;color:var(--green);letter-spacing:.5px;display:flex;align-items:center;gap:10px}
.brand-mark{width:18px;height:18px;border-radius:50%;background:#e8931b}
.stamp{left:779px;top:25px;width:97px;height:97px;border-radius:50%;background:radial-gradient(circle at 40% 35%,#fbe37a,var(--gold) 60%,#d6a60e)}
.phone{left:907px;display:flex;align-items:center;gap:12px;font-size:19px;font-weight:700;color:#5a5a5a}
.flag{width:46px;height:30px;border:1px solid #999}
.flag-au{background:#1a2f7a}
.flag-br{background:#1d9a3c}
.nav{left:85px;top:148px;display:flex;gap:4px}
.tab{width:110.7px;height:47px;border-radius:6px 6px 0 0;background:linear-gradient(var(--orange-top),var(--orange-bot));color:var(--tab-text);font-family:"Questrial",sans-serif;font-size:17px;display:flex;align-items:center;justify-content:center;text-align:center;line-height:15px;position:relative}
.tab.is-light{background:linear-gradient(#fbd698,#f2b45b)}
.tab.is-active::after{content:"";position:absolute;bottom:0;left:50%;margin-left:-6px;border:6px solid transparent;border-bottom-color:#fff}
.card{left:74px;top:195px;width:1052px;background:#fff;border-radius:6px 6px 0 0}
.footer{left:0;width:1200px;background:linear-gradient(var(--green),var(--green-dark))}
.foot-logo{left:85px;top:30px;font-family:"Questrial",sans-serif;font-size:36px;color:#fff;letter-spacing:.5px}
.foot-copy{left:115px;top:74px;font-size:12px;color:#bfe8cf}
.foot-div{left:426px;top:18px;width:1px;height:88px;background:#3cb778}
.foot-col{list-style:none;font-size:13px;color:#e6f6ec;line-height:27.5px;top:20px}
.foot-col li::before{content:"•";margin-right:10px;color:#bfe8cf}
.partners-title{left:920px;top:22px;font-size:12px;font-weight:700;color:#fff}
.partner{top:46px;width:92px;height:31px;border:1px solid #7fd6a6;background:#14b064}
.quote{width:328px;height:263px;background:linear-gradient(#fff 80%,#ececec);border-radius:5px}
.quote-head{left:0;top:0;width:328px;height:44px;border-radius:4px;background:linear-gradient(#12ad63,var(--green-dark));color:#fff;font-family:"Questrial",sans-serif;font-size:22px;padding:9px 0 0 35px}
.quote-head svg{position:absolute;left:14px;top:13px}
.q-label{font-family:"Questrial",sans-serif;font-size:22px;color:var(--blue)}
.radios{left:11px;top:93px;list-style:none;font-size:13px;color:#555;line-height:19.7px}
.radios li{display:flex;align-items:center;gap:9px}
.radio{width:13px;height:13px;border-radius:50%;border:1px solid #8a9bb8;background:#fff;position:relative}
.radio.is-on::after{content:"";position:absolute;left:3px;top:3px;width:5px;height:5px;border-radius:50%;background:#2a9a4a}
.select{left:157px;top:95px;width:160px;height:21px;border:1px solid #8aa3c8;font-size:13px;padding:1px 5px;background:#fff}
.select span{position:absolute;right:1px;top:1px;width:17px;height:17px;background:linear-gradient(#e4ecf8,#b9cbe6)}
.btn{height:27px;border-radius:6px;background:linear-gradient(#e8e8e8,#bdbdbd);color:#666;font-size:14px;display:flex;align-items:center;justify-content:center}
.cards{left:157px;top:164px;display:flex;gap:9px}
.pay{width:33px;height:21px;border-radius:2px}
.box-head{height:44px;border-radius:5px;background:linear-gradient(#2f6ab8,var(--blue-dark));color:#fff;font-family:"Questrial",sans-serif;font-size:22px;padding:10px 0 0 12px}
.deals{list-style:none;font-size:13px}
.deals li{display:flex;justify-content:space-between;height:27.3px;align-items:center;padding:0 0 0 10px;border-bottom:1px solid var(--line)}
.deals b{color:var(--red);width:130px}
.more{font-size:12px;color:var(--link-green)}
.form-label{font-size:13px;font-weight:700;color:var(--blue)}
.field{border:1px solid #9db2cf;background:#fff;height:22px}
.photo{border-radius:3px}
.offer{width:332px;height:166px}
.offer .photo{left:0;top:4px;width:96px;height:106px}
.offer h3{position:absolute;left:110px;top:0;font-family:"Questrial",sans-serif;font-weight:400;font-size:22px;color:var(--blue)}
.offer p{position:absolute;left:110px;top:32px;width:218px;font-size:13px;line-height:19.7px;color:#555}
.offer .more{position:absolute;left:110px}
.hr{height:1px;background:var(--line)}
.crumb{font-size:12px;font-weight:700;color:var(--blue)}
.title{font-family:"Questrial",sans-serif;font-size:34px;color:var(--blue)}
.subtitle{font-family:"Questrial",sans-serif;font-size:25px;color:#13a060}
.copy{font-size:13px;line-height:19.7px;color:#555}
.quick{border:1px solid #dcdcdc;border-radius:5px;background:linear-gradient(#fff 70%,#f0f0f0)}
.quick h4{position:absolute;left:13px;top:14px;font-family:"Questrial",sans-serif;font-weight:400;font-size:23px;color:var(--blue)}
.quick ul{position:absolute;list-style:none;font-size:12px;font-weight:700;color:#777;line-height:19.7px}
.quick li::before{content:"›";color:#f08c10;font-size:16px;margin-right:10px}
</style>
</head>
<body>

<!-- Home page -->
<section class="page page-home">
  <div class="abs head-bg"></div>
  <div class="abs band" style="height:986px"></div>
  <div class="abs brand"><span class="brand-mark"></span>Idiomas Corvalo</div>
  <div class="abs stamp" role="img" aria-label="Gold best price credibility seal"></div>
  <div class="abs phone" style="top:31px"><span class="flag flag-au" role="img" aria-label="Australian flag"></span>0 800 555 010</div>
  <div class="abs phone" style="top:83px"><span class="flag flag-br" role="img" aria-label="Brazilian flag"></span>1 800 555 020</div>
  <nav class="abs nav">
    <div class="tab is-active">Home</div><div class="tab">Promocoes</div><div class="tab">Cidades</div><div class="tab">Escolas</div><div class="tab">Passagem<br>Aerea</div><div class="tab">Visto</div><div class="tab">Embarque</div><div class="tab">Contacto</div><div class="tab is-light">Blog</div>
  </nav>

  <main class="abs card" style="height:966px">
    <div class="abs photo" style="left:22px;top:21px;width:660px;height:262px;background:linear-gradient(100deg,#b58567 0%,#5f7fb4 30%,#a44a3a 55%,#5c4a3e 75%,#3d3f4a 100%)" role="img" aria-label="Smiling young student in front of a group of friends on campus"></div>
    <div class="abs" style="left:574px;top:254px;display:flex;gap:6px">
      <svg width="20" height="20"><circle cx="10" cy="10" r="9" fill="#777" opacity=".8"/><path d="M10 5v10M5 10h10" stroke="#fff" stroke-width="3"/></svg>
      <svg width="20" height="20"><circle cx="10" cy="10" r="9" fill="#777" opacity=".8"/><path d="M10 5v10M5 10h10" stroke="#fff" stroke-width="3"/></svg>
      <svg width="20" height="20"><circle cx="10" cy="10" r="9" fill="#777" opacity=".8"/><path d="M10 5v10M5 10h10" stroke="#fff" stroke-width="3"/></svg>
      <svg width="20" height="20"><circle cx="10" cy="10" r="9" fill="#777" opacity=".8"/><path d="M10 5v10M5 10h10" stroke="#fff" stroke-width="3"/></svg>
    </div>

    <div class="abs quote" style="left:704px;top:20px">
      <div class="abs quote-head"><svg width="10" height="18"><path d="M1 1l7 8-7 8" fill="none" stroke="#7fe0a8" stroke-width="2"/></svg>COTAÇÃO ON-LINE</div>
      <div class="abs q-label" style="left:11px;top:55px">Cidade</div>
      <div class="abs q-label" style="left:157px;top:55px">Duração</div>
      <ul class="abs radios">
        <li><span class="radio is-on"></span>Sydney</li><li><span class="radio"></span>Melbourne</li><li><span class="radio"></span>Gold Coast</li><li><span class="radio"></span>Brisbane</li><li><span class="radio"></span>Perth</li><li><span class="radio"></span>Adelaide</li><li><span class="radio"></span>Byron Bay</li>
      </ul>
      <div class="abs select">2 Semanas<span></span></div>
      <div class="abs btn" style="left:157px;top:133px;width:80px">Procurar</div>
      <div class="abs cards"><span class="pay" style="background:#2c4ea0"></span><span class="pay" style="background:#e0401c"></span><span class="pay" style="background:#2a7cc4"></span><span class="pay" style="background:#dfe6f0;border:1px solid #aab"></span></div>
    </div>

    <div class="abs" style="left:22px;top:306px;width:305px">
      <div class="box-head">IN AUSTRALIA</div>
      <ul class="deals" style="margin-top:4px">
        <li>Brisbane<b>From $89</b></li><li>Ballina Byron Bay<b>From $79</b></li><li>Gold Coast<b>From $75</b></li><li>Hamilton Island<b>From $159</b></li><li style="border:0">Launceston<b>From $89</b></li>
      </ul>
      <div style="height:40px;border-radius:0 0 5px 5px;background:linear-gradient(#fff,#ebebeb);border-top:1px solid var(--line);text-align:right;padding:12px 14px 0 0"><span class="more">More Domestic Flights</span></div>
    </div>

    <div class="abs" style="left:22px;top:550px;width:305px;height:397px;border-radius:5px;background:linear-gradient(#fff 85%,#ececec)">
      <div class="box-head">ENTRE EM CONTATO</div>
      <p class="abs copy" style="left:10px;top:55px;width:270px">Lorem ipsum dolor sit amet, consectetur adipiscing elit. Proin ut lectus non nunc</p>
      <div class="abs form-label" style="left:10px;top:98px">Nome</div>
      <div class="abs field" style="left:10px;top:120px;width:283px"></div>
      <div class="abs form-label" style="left:10px;top:155px">E-mail</div>
      <div class="abs form-label" style="left:164px;top:155px">Telefone</div>
      <div class="abs field" style="left:10px;top:177px;width:130px"></div>
      <div class="abs field" style="left:164px;top:177px;width:130px"></div>
      <div class="abs form-label" style="left:10px;top:214px">Mensagem</div>
      <div class="abs field" style="left:10px;top:236px;width:283px;height:102px"></div>
      <div class="abs btn" style="left:10px;top:356px;width:68px">Send</div>
    </div>

    <article class="abs offer" style="left:350px;top:302px"><div class="abs photo" style="background:linear-gradient(135deg,#e8c7a6,#d85a3a)" role="img" aria-label="Young child resting on a book"></div><h3>Brightkids</h3><p>Help improve the lives of some of the world's poorest children.</p><span class="more" style="top:84px">See more</span></article>
    <article class="abs offer" style="left:702px;top:302px"><div class="abs photo" style="background:linear-gradient(135deg,#9ccf5a,#2d6a22)" role="img" aria-label="Green world map"></div><h3>Where we fly</h3><p>International and domestic route maps.</p><span class="more" style="top:84px">See more</span></article>
    <div class="abs hr" style="left:350px;top:448px;width:306px"></div><div class="abs hr" style="left:702px;top:448px;width:332px"></div>
    <article class="abs offer" style="left:350px;top:468px"><div class="abs photo" style="background:linear-gradient(#d7ecfa,#4ea2e0)" role="img" aria-label="Girl jumping against a blue sky"></div><h3>Activities</h3><p>Endless Summer Pass for Gold Coast Theme Parks and other great activities.</p><span class="more" style="top:104px">See more</span></article>
    <article class="abs offer" style="left:702px;top:468px"><div class="abs photo" style="background:linear-gradient(135deg,#555,#111 60%,#c98a2a)" role="img" aria-label="Car headlight close-up"></div><h3>Cars</h3><p>Discounted cars rental rates from Rodan and Velo. Plus earn Skyroo Frecuent Flyer Points.</p><span class="more" style="top:104px">See more</span></article>
    <div class="abs hr" style="left:350px;top:619px;width:306px"></div><div class="abs hr" style="left:702px;top:619px;width:332px"></div>
    <article class="abs offer" style="left:350px;top:638px"><div class="abs photo" style="background:linear-gradient(135deg,#b47a52,#e2405a)" role="img" aria-label="Smiling young girl"></div><h3>Brightkids</h3><p>Help improve the lives of some of the world's poorest children.</p><span class="more" style="top:84px">See more</span></article>
    <article class="abs offer" style="left:702px;top:638px"><div class="abs photo" style="background:linear-gradient(135deg,#9ccf5a,#2d6a22)" role="img" aria-label="Green world map"></div><h3>Where we fly</h3><p>International and domestic route maps.</p><span class="more" style="top:84px">See more</span></article>
    <div class="abs hr" style="left:350px;top:786px;width:306px"></div><div class="abs hr" style="left:702px;top:786px;width:332px"></div>
    <article class="abs offer" style="left:350px;top:806px"><div class="abs photo" style="background:linear-gradient(#d7ecfa,#4ea2e0)" role="img" aria-label="Girl jumping against a blue sky"></div><h3>Activities</h3><p>Endless Summer Pass for Gold Coast Theme Parks and other great activities.</p><span class="more" style="top:104px">See more</span></article>
    <article class="abs offer" style="left:702px;top:806px"><div class="abs photo" style="background:linear-gradient(135deg,#555,#111 60%,#c98a2a)" role="img" aria-label="Car headlight close-up"></div><h3>Cars</h3><p>Discounted cars rental rates from Rodan and Velo. Plus earn Skyroo Frecuent Flyer Points.</p><span class="more" style="top:104px">See more</span></article>
    <div class="abs hr" style="left:350px;top:943px;width:306px"></div><div class="abs hr" style="left:702px;top:943px;width:332px"></div>
  </main>

  <footer class="abs footer" style="top:1161px;height:120px">
    <div class="abs foot-logo">IDIOMAS CORVALO</div>
    <div class="abs foot-copy">Copyright 2009 &nbsp;|&nbsp; idiomascorvalo.com.br</div>
    <div class="abs foot-div"></div>
    <ul class="abs foot-col" style="left:454px"><li>HOME</li><li>PROMOCOES</li><li>CIDADES</li></ul>
    <ul class="abs foot-col" style="left:607px"><li>ESCOLAS</li><li>PASSAGEM AEREA</li><li>VISTO</li></ul>
    <ul class="abs foot-col" style="left:784px"><li>EMBARQUE</li><li>CONTATO</li><li>BLOG</li></ul>
    <div class="abs partners-title">PARTNERS</div>
    <div class="abs partner" style="left:920px"></div>
    <div class="abs partner" style="left:1021px"></div>
  </footer>
</section>

<!-- Interior page -->
<section class="page page-inner">
  <div class="abs head-bg"></div>
  <div class="abs band" style="height:1094px"></div>
  <div class="abs brand"><span class="brand-mark"></span>Idiomas Corvalo</div>
  <div class="abs stamp" role="img" aria-label="Gold best price credibility seal"></div>
  <div class="abs phone" style="top:31px"><span class="flag flag-au" role="img" aria-label="Australian flag"></span>0 800 555 010</div>
  <div class="abs phone" style="top:83px"><span class="flag flag-br" role="img" aria-label="Brazilian flag"></span>1 800 555 020</div>
  <nav class="abs nav">
    <div class="tab">Home</div><div class="tab is-active">Promocoes</div><div class="tab">Cidades</div><div class="tab">Escolas</div><div class="tab">Passagem<br>Aerea</div><div class="tab">Visto</div><div class="tab">Embarque</div><div class="tab">Contacto</div><div class="tab is-light">Blog</div>
  </nav>

  <main class="abs card" style="height:1074px">
    <div class="abs crumb" style="left:24px;top:38px">Home &nbsp;-&nbsp; Promocoes</div>
    <h1 class="abs title" style="left:22px;top:60px;font-weight:400">Tittle 1</h1>
    <div class="abs photo" style="left:22px;top:116px;width:305px;height:340px;background:linear-gradient(#e4e6ea,#cfd2d8 60%,#f0f0f0)" role="img" aria-label="Stack of books"></div>
    <p class="abs copy" style="left:347px;top:120px;width:328px">Lorem ipsum dolor sit amet, consectetur adipiscing elit. Maecenas nec nisl ut mauris dapibus congue. Nunc et orci at urna suscipit faucibus. Integer vitae sapien libero. Nulla tincidunt venenatis accumsan. Integer sit amet sem eget urna tempus faucibus. Aenean cursus sapien diam. Phasellus euismod eros a lorem vulputate at porta ante fringilla. Suspendisse ac purus et purus rutrum vestibulum vitae in magna. Mauris sollicitudin dapibus tristique. Cras convallis, nibh a tempor cursus, mi nunc tempus lacus, id malesuada lectus enim non lorem. In commodo erat vel eros iaculis eget hendrerit augue accumsan. Duis non ultricies justo. Vestibulum ante ipsum primis in faucibus orci luctus et ultrices posuere cubilia Curae; Nunc auctor tincidunt tortor, in auctor sem rhoncus eu. Praesent posuere tincidunt nisl eget consequat. Vivamus imperdiet quam quis nulla porta laoreet. Donec et tellus magna, tempus interdum velit. Sed rutrum dignissim lorem a gravida. Nunc vel velit ut</p>
    <h2 class="abs subtitle" style="left:22px;top:498px;font-weight:400">Subtitle 1</h2>
    <p class="abs copy" style="left:22px;top:532px;width:662px">Donec vestibulum, tellus tempor ullamcorper sodales, diam sapien sollicitudin orci, eget viverra quam urna eget turpis. Nullam libero mi, mattis et tempor sit amet, semper sit amet sapien. Quisque molestie elementum dignissim. Aliquam molestie, odio eu tristique vehicula, dui leo luctus leo, eu porta diam leo quis augue. Quisque gravida euismod malesuada. Nam sit amet risus in dolor blandit pharetra. Integer lacinia vehicula velit vitae scelerisque. Nulla in orci sapien, id aliquam nulla. Maecenas luctus sem at ipsum porta elementum. Duis in felis elit, non molestie turpis. Nullam lobortis rhoncus tincidunt. Phasellus vitae tempus sapien. Cras pretium, nunc in vulputate molestie, purus ipsum elementum mi, sit amet fringilla nulla magna non urna. Duis vitae tincidunt lectus. Nullam placerat neque in enim volutpat luctus nec eu ante. Nunc interdum arcu nec tellus ultrices ut fringilla leo fermentum. Donec quam urna, rhoncus vitae malesuada imperdiet, eleifend iaculis dolor. Cras aliquam vestibulum ornare. Vestibulum lorem velit, placerat et sodales ac, aliquet et lorem.</p>

    <div class="abs quote" style="left:704px;top:20px">
      <div class="abs quote-head"><svg width="10" height="18"><path d="M1 1l7 8-7 8" fill="none" stroke="#7fe0a8" stroke-width="2"/></svg>COTAÇÃO ON-LINE</div>
      <div class="abs q-label" style="left:11px;top:55px">Cidade</div>
      <div class="abs q-label" style="left:157px;top:55px">Duração</div>
      <ul class="abs radios">
        <li><span class="radio is-on"></span>Sydney</li><li><span class="radio"></span>Melbourne</li><li><span class="radio"></span>Gold Coast</li><li><span class="radio"></span>Brisbane</li><li><span class="radio"></span>Perth</li><li><span class="radio"></span>Adelaide</li><li><span class="radio"></span>Byron Bay</li>
      </ul>
      <div class="abs select">2 Semanas<span></span></div>
      <div class="abs btn" style="left:157px;top:133px;width:80px">Procurar</div>
      <div class="abs cards"><span class="pay" style="background:#2c4ea0"></span><span class="pay" style="background:#e0401c"></span><span class="pay" style="background:#2a7cc4"></span><span class="pay" style="background:#dfe6f0;border:1px solid #aab"></span></div>
    </div>

    <div class="abs" style="left:704px;top:306px;width:328px;height:527px;border-radius:5px;background:linear-gradient(#fff 88%,#ececec)">
      <div class="box-head">AJUDA</div>
      <div class="abs photo" style="left:2px;top:57px;width:326px;height:100px;background:linear-gradient(90deg,#2f5f7a,#8fb3c2 45%,#d8b39a 75%,#b98d72)" role="img" aria-label="Support agent with a headset"></div>
      <p class="abs copy" style="left:11px;top:168px;width:300px">Tiré aquí suas duvidas. Entraremos em contato como voce em poucos instantes!</p>
      <div class="abs form-label" style="left:11px;top:214px">Nome</div>
      <div class="abs field" style="left:11px;top:236px;width:306px"></div>
      <div class="abs form-label" style="left:11px;top:271px">E-mail</div>
      <div class="abs form-label" style="left:177px;top:271px">Telefone</div>
      <div class="abs field" style="left:11px;top:293px;width:140px"></div>
      <div class="abs field" style="left:177px;top:293px;width:140px"></div>
      <div class="abs form-label" style="left:11px;top:330px">Mensagem</div>
      <div class="abs field" style="left:11px;top:352px;width:306px;height:102px"></div>
      <div class="abs btn" style="left:11px;top:470px;width:78px">Procurar</div>
    </div>

    <div class="abs quick" style="left:704px;top:857px;width:328px;height:188px">
      <h4>ACESSO RÁPIDO</h4>
      <ul style="left:20px;top:62px"><li>Escolas</li><li>Cidades</li><li>Acomodação</li><li>Visto</li><li>Seguro - Saude</li><li>Passagem Aérea</li></ul>
      <ul style="left:167px;top:62px;width:150px;line-height:16px"><li style="margin-bottom:4px">Formas de<br>&nbsp;&nbsp;&nbsp;&nbsp;&nbsp;Pagamento</li><li style="margin-bottom:4px">Compra de dólares</li><li style="margin-bottom:4px">FAQS</li><li>Sobre Nos</li></ul>
    </div>
  </main>

  <footer class="abs footer" style="top:1269px;height:124px">
    <div class="abs foot-logo">IDIOMAS CORVALO</div>
    <div class="abs foot-copy">Copyright 2009 &nbsp;|&nbsp; idiomascorvalo.com.br</div>
    <div class="abs foot-div"></div>
    <ul class="abs foot-col" style="left:454px"><li>HOME</li><li>PROMOCOES</li><li>CIDADES</li></ul>
    <ul class="abs foot-col" style="left:607px"><li>ESCOLAS</li><li>PASSAGEM AEREA</li><li>VISTO</li></ul>
    <ul class="abs foot-col" style="left:784px"><li>EMBARQUE</li><li>CONTATO</li><li>BLOG</li></ul>
    <div class="abs partners-title">PARTNERS</div>
    <div class="abs partner" style="left:920px"></div>
    <div class="abs partner" style="left:1021px"></div>
  </footer>
</section>

</body>
</html>
```